MORVA Design

We have a 5 part framework that companies use to plot their social media strategies and digital transformation activity. We would like to display the 5 elements in a circular format (please see the attachment for our current design - we want to get a better version of that).

The five elements and their meaning can be read about here: http://quellagrove.example/morva/what-is-morva/
We would like to see designs that fit our corporate image but also maintain informality and simplicity…. Ive included another image of some of the icons we've been using and enjoying to give an understanding of the stuff we like

Target Market(s)

Corporates

Industry/Entity Type

Digital

Logo Text

Brokerage, Integration, Trust, Incentives, Leadership

Colors
0255a3

Requirements
Must have
• Must be circular in format with each element neatly labelled - PLEASE REVIEW OUR CURRENT VERSION IN THE ATTACHMENTS

```html
<!DOCTYPE html>
<html lang="en">
<head>
<meta charset="utf-8">
<title>MORVA Framework</title>
<link rel="stylesheet" href="https://fonts.googleapis.com/css2?family=Open+Sans:wght@400;700&display=swap">
<style>
  :root {
    --brand-navy: #0255a3;
    --brand-sky: #00a7e5;
    --ink-white: #ffffff;
    --canvas: #ffffff;
  }
  html, body {
    margin: 0;
    padding: 0;
    width: 1200px;
    height: 1000px;
    overflow: hidden;
    background: var(--canvas);
  }
  .framework {
    display: block;
    width: 1200px;
    height: 1000px;
    font-family: "Open Sans", Arial, sans-serif;
  }
  .framework__ring { fill: none; stroke: var(--brand-navy); stroke-width: 20; }
  .framework__hub { fill: var(--brand-navy); }
  .framework__hub-label { fill: var(--ink-white); font-size: 13px; font-weight: 400; text-anchor: middle; }
  .element__disc { fill: var(--brand-sky); }
  .element__letter { fill: var(--ink-white); font-size: 23px; font-weight: 700; text-anchor: middle; }
  .element__label { fill: var(--ink-white); font-size: 13px; font-weight: 400; text-anchor: middle; }
  .icon { fill: var(--ink-white); stroke: none; }
  .icon--line { fill: none; stroke: var(--ink-white); stroke-width: 2.4; stroke-linecap: round; stroke-linejoin: round; }
  .icon__mark { fill: var(--brand-sky); font-size: 9px; font-weight: 700; text-anchor: middle; }
</style>
</head>
<body>
<svg class="framework" viewBox="0 0 1200 1000" role="img" aria-label="Five part framework: Brokerage, Integration, Trust Building, Incentives and Leadership around Community Management">
  <circle class="framework__ring" cx="600" cy="523" r="161"/>

  <g class="framework__hub">
    <circle cx="600" cy="523" r="61"/>
    <text class="framework__hub-label" x="600" y="520">Community</text>
    <text class="framework__hub-label" x="600" y="535">Management</text>
  </g>

  <!-- Brokerage -->
  <g class="element element--brokerage" transform="translate(600 362)">
    <circle class="element__disc" r="61"/>
    <circle class="icon" cx="-2" cy="-33" r="9"/>
    <circle cx="-2" cy="-33" r="6.5" fill="none" stroke="#00a7e5" stroke-width="1.2"/>
    <text class="icon__mark" x="-2" y="-30">$</text>
    <path class="icon--line" d="M-20 -19 q4 -4 9 -1 l6 3 h8 M-20 -19 q6 6 14 6 h9 q4 0 8 -4"/>
    <rect class="icon" x="14" y="-24" width="6" height="12" rx="1"/>
    <text class="element__letter" x="0" y="20">B</text>
    <text class="element__label" x="0" y="38">Brokerage</text>
  </g>

  <!-- Integration -->
  <g class="element element--integration" transform="translate(748 451)">
    <circle class="element__disc" r="61"/>
    <rect class="icon--line" x="-23" y="-28" width="26" height="16" rx="8" stroke-width="4"/>
    <rect class="icon--line" x="-3" y="-28" width="26" height="16" rx="8" stroke-width="4"/>
    <text class="element__letter" x="0" y="20">I</text>
    <text class="element__label" x="0" y="38">Integration</text>
  </g>

  <!-- Trust Building -->
  <g class="element element--trust" transform="translate(717 637)">
    <circle class="element__disc" r="61"/>
    <rect class="icon" x="-36" y="-38" width="9" height="16" rx="1" transform="rotate(20 -31 -30)"/>
    <rect class="icon" x="27" y="-38" width="9" height="16" rx="1" transform="rotate(-20 31 -30)"/>
    <path class="icon--line" d="M-26 -32 q10 -6 20 -2 l8 3 l10 -5 q8 -2 14 2 M-24 -24 l10 8 q4 3 8 0 l10 -6 l6 -4 M-10 -18 l6 5 M-3 -20 l6 5"/>
    <text class="element__letter" x="0" y="20">T</text>
    <text class="element__label" x="0" y="38">Trust Building</text>
  </g>

  <!-- Incentives -->
  <g class="element element--incentives" transform="translate(486 637)">
    <circle class="element__disc" r="61"/>
    <rect class="icon" x="-22" y="-36" width="44" height="18" rx="1"/>
    <circle cx="0" cy="-27" r="6" fill="none" stroke="#00a7e5" stroke-width="1.4"/>
    <text class="icon__mark" x="0" y="-24">$</text>
    <rect class="icon" x="-22" y="-16" width="44" height="1.6"/>
    <rect class="icon" x="-21" y="-13" width="42" height="1.6"/>
    <rect class="icon" x="-20" y="-10" width="40" height="1.6"/>
    <text class="element__letter" x="0" y="20">I</text>
    <text class="element__label" x="0" y="38">Incentives</text>
  </g>

  <!-- Leadership -->
  <g class="element element--leadership" transform="translate(452 451)">
    <circle class="element__disc" r="61"/>
    <circle class="icon" cx="-15" cy="-34" r="5"/>
    <circle class="icon" cx="15" cy="-34" r="5"/>
    <path class="icon" d="M-23 -12 v-10 q0 -6 8 -6 q8 0 8 6 v10 z M7 -12 v-10 q0 -6 8 -6 q8 0 8 6 v10 z"/>
    <circle cx="0" cy="-37" r="7" class="icon" stroke="#00a7e5" stroke-width="1.5"/>
    <path class="icon" d="M-11 -8 v-13 q0 -8 11 -8 q11 0 11 8 v13 z" stroke="#00a7e5" stroke-width="1.5"/>
    <text class="element__letter" x="0" y="20">L</text>
    <text class="element__label" x="0" y="38">Leadership</text>
  </g>
</svg>
</body>
</html>
```